Visitenkarten für den Verkauf mediterraner Pflanzen
Zielgruppe
Verkauf winterharter mediterraner Pflanzen
Aufgabenstellung
Die Farben von der Homepage und eventuell die Schriftarten sollten übernommen werden um ein einheitliches Erscheinungsbild zu erzeugen

```html
<!DOCTYPE html>
<html lang="de">
<head>
<meta charset="utf-8">
<title>Verdanto – Visitenkarten</title>
<link rel="stylesheet" href="https://fonts.googleapis.com/css2?family=Saira:wght@400;500&family=Fredoka:wght@500;600&display=swap">
<style>
  :root {
    --backdrop: #a9c7b4;
    --card-light: #e3eeea;
    --card-light-shade: #d3e3de;
    --card-teal: #63a192;
    --card-teal-deep: #3f7362;
    --label-green: #5fa592;
    --ink: #1f2a2e;
    --brand-green: #5bb97c;
    --text-light: #e8f3ef;
    --title-dark: #2e5548;
  }
  * { margin: 0; padding: 0; box-sizing: border-box; }
  html, body { width: 1200px; height: 892px; overflow: hidden; }
  body {
    background: var(--backdrop);
    font-family: "Saira", sans-serif;
    position: relative;
  }
  .card {
    position: absolute;
    top: 300px;
    width: 470px;
    height: 290px;
    border-radius: 3px;
    box-shadow: 0 24px 40px rgba(40, 80, 65, 0.25);
    overflow: hidden;
  }
  .card--front {
    left: 80px;
    background: linear-gradient(160deg, var(--card-light), var(--card-light-shade));
    border-bottom: 6px solid var(--card-teal);
  }
  .card--back { left: 650px; }

  .brand {
    position: absolute;
    top: 34px;
    right: 34px;
    display: flex;
    align-items: center;
    gap: 12px;
  }
  .brand__dot {
    width: 52px; height: 52px;
    border-radius: 50%;
    background: var(--brand-green);
  }
  .brand__name {
    font-size: 26px;
    font-weight: 500;
    letter-spacing: 2px;
    color: var(--ink);
    text-transform: uppercase;
  }

  .contact {
    position: absolute;
    left: 40px;
    top: 118px;
    display: grid;
    grid-template-columns: 96px auto;
    row-gap: 6px;
    font-size: 15px;
    line-height: 1.25;
  }
  .contact__label {
    font-family: "Fredoka", sans-serif;
    font-weight: 600;
    font-size: 14px;
    color: var(--label-green);
    text-transform: uppercase;
  }
  .contact__value { color: var(--ink); }

  .social {
    position: absolute;
    left: 40px;
    bottom: 28px;
    display: flex;
    gap: 26px;
  }
  .social__dot {
    width: 18px; height: 18px;
    border-radius: 50%;
    border: 2px solid var(--ink);
  }

  .card__foliage { position: absolute; inset: 0; }
  .back__content {
    position: absolute;
    inset: 0;
    display: flex;
    flex-direction: column;
    align-items: center;
    justify-content: center;
    text-align: center;
    padding-left: 60px;
  }
  .back__title {
    font-size: 24px;
    font-weight: 500;
    letter-spacing: 1px;
    color: var(--title-dark);
    margin-bottom: 18px;
  }
  .back__claim {
    font-size: 17px;
    line-height: 1.45;
    color: var(--text-light);
  }
</style>
</head>
<body>
  <section class="card card--front" aria-label="Visitenkarte Vorderseite">
    <div class="brand">
      <span class="brand__dot" aria-hidden="true"></span>
      <span class="brand__name">Verdanto</span>
    </div>
    <dl class="contact">
      <dt class="contact__label">Adresse</dt>
      <dd class="contact__value">Birkenweg 12<br>8010, Österreich</dd>
      <dt class="contact__label">Web</dt>
      <dd class="contact__value">www.verdanto.at</dd>
      <dt class="contact__label">Telefon</dt>
      <dd class="contact__value">+43 (0)660 4817302</dd>
      <dt class="contact__label">E-Mail</dt>
      <dd class="contact__value">office@verdanto.at</dd>
    </dl>
    <div class="social" aria-hidden="true">
      <span class="social__dot"></span>
      <span class="social__dot"></span>
      <span class="social__dot"></span>
    </div>
  </section>

  <section class="card card--back" aria-label="Visitenkarte Rückseite">
    <svg class="card__foliage" viewBox="0 0 470 290" preserveAspectRatio="none" role="img" aria-label="Hintergrund mit Monstera- und Palmblättern in Grüntönen">
      <defs>
        <linearGradient id="foliage-tone" x1="0" y1="0" x2="1" y2="1">
          <stop offset="0" stop-color="#4f8a76"/>
          <stop offset="0.45" stop-color="#63a192"/>
          <stop offset="1" stop-color="#5a9886"/>
        </linearGradient>
      </defs>
      <rect width="470" height="290" fill="url(#foliage-tone)"/>
    </svg>
    <div class="back__content">
      <h2 class="back__title">VERDANTO</h2>
      <p class="back__claim">Dein Spezialist für Palmen<br>und exotische Pflanzen</p>
    </div>
  </section>
</body>
</html>
```